Real Estate Development Company Stationary

We need our company, business card, letterhead, pocket folder and envelope designed.

We are a new real estate development company. We focus on data centre, commercial and real estate development.

Please see attached for our logo. Since it's a new logo, you still can make minor adjust if you like it makes senses

The client has sent me a business card he really likes. Please see file 3.

Target Market(s)

Real Estate Investors
Large corporations
Home buyers

Industry/Entity Type

Real Estate

```html
<!DOCTYPE html>
<html lang="en">
<head>
<meta charset="UTF-8">
<title>Kevra Development Inc. – Business Card</title>
<link rel="stylesheet" href="https://fonts.googleapis.com/css2?family=Jost:ital,wght@0,400;0,500;1,400&display=swap">
<style>
  :root {
    --bg: #33414b;
    --navy: #0e4487;
    --pale-blue: #b7c8df;
    --green: #6cb33f;
    --ink: #1f1f1f;
    --paper: #ffffff;
    --label: #ffffff;
  }
  * { box-sizing: border-box; margin: 0; padding: 0; }
  html, body {
    width: 1200px; height: 1000px; overflow: hidden;
    background: var(--bg);
    font-family: "Jost", "Futura", sans-serif;
  }
  .canvas { position: relative; width: 1200px; height: 1000px; }
  .sheet-title {
    position: absolute; left: 34px; top: 26px;
    color: var(--label); font-size: 36px; font-weight: 400;
  }
  .card {
    position: absolute; left: 240px; width: 720px;
    overflow: hidden;
    box-shadow: 0 18px 40px rgba(0,0,0,.35);
  }
  .card-front { top: 100px; height: 420px; background: var(--navy); }
  .card-back { top: 545px; height: 430px; background: var(--paper); }

  .brand { position: absolute; display: flex; align-items: center; }
  .brand-mark { border-radius: 50%; flex: none; }
  .brand-name { font-weight: 500; white-space: nowrap; }

  .card-front .brand { left: 70px; top: 170px; gap: 22px; }
  .card-front .brand-mark { width: 70px; height: 70px; background: var(--pale-blue); }
  .card-front .brand-name { color: var(--pale-blue); font-size: 46px; }

  .card-back .brand { left: 30px; top: 80px; gap: 16px; }
  .card-back .brand-mark { width: 54px; height: 54px; background: var(--green); }
  .card-back .brand-name { color: var(--green); font-size: 34px; }

  .holder { position: absolute; right: 48px; top: 166px; text-align: right; }
  .holder-name { font-size: 22px; font-weight: 500; color: var(--ink); line-height: 30px; }
  .holder-role { font-size: 17px; color: var(--navy); line-height: 26px; }

  .contact-list {
    position: absolute; right: 26px; top: 248px; list-style: none;
    font-size: 21px; color: var(--ink); line-height: 30px;
  }
  .contact-list li { display: flex; justify-content: flex-end; align-items: center; gap: 10px; }
  .contact-list svg { width: 19px; height: 19px; flex: none; }

  .address {
    position: absolute; left: 48px; top: 322px;
    font-size: 20px; font-style: italic; color: var(--ink); line-height: 27px;
  }
  .band-green { position: absolute; left: 0; right: 0; bottom: 36px; height: 8px; background: var(--green); }
  .band-navy { position: absolute; left: 0; right: 0; bottom: 0; height: 36px; background: var(--navy); }
</style>
</head>
<body>
<main class="canvas">
  <h1 class="sheet-title">Business Card</h1>

  <section class="card card-front" aria-label="Business card front">
    <div class="brand">
      <span class="brand-mark"></span>
      <span class="brand-name">Kevra Development Inc.</span>
    </div>
  </section>

  <section class="card card-back" aria-label="Business card back">
    <div class="brand">
      <span class="brand-mark"></span>
      <span class="brand-name">Kevra Development Inc.</span>
    </div>

    <div class="holder">
      <p class="holder-name">Lena Marsh</p>
      <p class="holder-role">Project Manager</p>
    </div>

    <ul class="contact-list">
      <li>416-555-0142
        <svg viewBox="0 0 18 18" aria-hidden="true"><rect x="5" y="1" width="8" height="16" rx="1.5" fill="none" stroke="var(--navy)" stroke-width="1.6"/><line x1="8" y1="14.5" x2="10" y2="14.5" stroke="var(--navy)" stroke-width="1.4"/></svg>
      </li>
      <li>416-555-0187
        <svg viewBox="0 0 18 18" aria-hidden="true"><path d="M1 6c0-2 3.5-3 8-3s8 1 8 3v1.5h-4V6H5v1.5H1z" fill="var(--navy)"/><rect x="3" y="9" width="12" height="7" rx="1.5" fill="var(--navy)"/></svg>
      </li>
      <li>lena.marsh@kevradev.ca
        <svg viewBox="0 0 18 18" aria-hidden="true"><rect x="1" y="3.5" width="16" height="11" fill="var(--navy)"/><path d="M1.5 4l7.5 6 7.5-6" fill="none" stroke="#fff" stroke-width="1.3"/></svg>
      </li>
      <li>www.kevradev.ca
        <svg viewBox="0 0 18 18" aria-hidden="true"><g fill="none" stroke="var(--navy)" stroke-width="1.4"><circle cx="9" cy="9" r="7.5"/><ellipse cx="9" cy="9" rx="3.3" ry="7.5"/><line x1="1.5" y1="9" x2="16.5" y2="9"/><path d="M3 5h12M3 13h12"/></g></svg>
      </li>
    </ul>

    <p class="address">Address Line 1<br>City, State, Zip Code</p>

    <div class="band-green"></div>
    <div class="band-navy"></div>
  </section>
</main>
</body>
</html>
```